Ledgerwise Business Card Design

Business Card Design for new business called Ledgerwise focused on selling business software to small and medium size companies who have outgrown Tallyhouse. Similar companies would be Tallyhouse, Vemo, BrightCore. Also Dealharbor would be good to look at for additional ideas around look and feel.

Target Market(s)

Business to Business

Industry/Entity Type

Information Technology

Contact Information for Business Card

Standard Business Card Information

Font styles to use
Sans Serif

```html
<!DOCTYPE html>
<html lang="en">
<head>
<meta charset="utf-8">
<title>Ledgerwise Business Card</title>
<link href="https://fonts.googleapis.com/css2?family=Open+Sans:wght@300;400;600;800&display=swap" rel="stylesheet">
<style>
  :root {
    --brand-blue: #0b5288;
    --brand-navy: #0e4d7e;
    --brand-orange: #f28a1e;
    --ink-grey: #555a60;
    --card-white: #ffffff;
    --backdrop: #e9e5df;
  }
  * { margin: 0; padding: 0; box-sizing: border-box; }
  html, body { width: 1200px; height: 843px; overflow: hidden; }
  body {
    background: var(--backdrop);
    font-family: "Open Sans", Arial, sans-serif;
    display: flex;
    flex-direction: column;
    align-items: center;
    justify-content: center;
    gap: 40px;
  }
  .card {
    position: relative;
    width: 640px;
    height: 366px;
    overflow: hidden;
    box-shadow: 0 6px 18px rgba(0,0,0,0.18);
  }

  /* Back side */
  .card--back { background: var(--brand-navy); }
  .back-mark {
    position: absolute;
    left: 0; right: 0; top: 150px;
    display: flex; align-items: center; justify-content: center; gap: 12px;
    color: var(--card-white);
    font-weight: 800;
    font-size: 34px;
    letter-spacing: 1px;
  }
  .back-mark .dot {
    width: 22px; height: 22px; border-radius: 50%;
    background: var(--card-white);
  }
  .back-url {
    position: absolute;
    left: 0; right: 0; top: 210px;
    text-align: center;
    color: var(--card-white);
    font-size: 13px;
    letter-spacing: 3px;
  }

  /* Front side */
  .card--front { background: var(--card-white); }
  .person { position: absolute; left: 40px; top: 52px; }
  .person-name {
    color: var(--brand-blue);
    font-weight: 400;
    font-size: 21px;
    letter-spacing: 0.5px;
  }
  .person-title {
    color: var(--brand-orange);
    font-size: 15px;
    margin-top: 2px;
  }
  .contact-list { list-style: none; margin-top: 14px; }
  .contact-list li {
    display: flex; align-items: center; gap: 10px;
    color: var(--ink-grey);
    font-size: 14px;
    line-height: 22px;
  }
  .contact-list svg { width: 13px; height: 13px; fill: var(--brand-blue); }
  .logo {
    position: absolute; right: 48px; top: 120px;
    display: flex; align-items: center; gap: 10px;
  }
  .logo-name {
    color: var(--brand-blue);
    font-weight: 800;
    font-size: 40px;
    letter-spacing: -0.5px;
  }
  .logo .dot {
    width: 30px; height: 30px; border-radius: 50%;
    background: var(--brand-orange);
  }
  .divider {
    position: absolute; left: 150px; right: 40px; top: 222px;
    height: 1px; background: var(--brand-orange);
  }
  .address {
    position: absolute; right: 48px; top: 238px;
    text-align: right;
    color: var(--ink-grey);
    font-size: 15px;
    line-height: 21px;
  }
  .bands { position: absolute; left: 0; bottom: 0; width: 640px; height: 44px; }
  .band-url {
    position: absolute; right: 48px; bottom: 10px;
    color: var(--card-white);
    font-size: 16px;
    letter-spacing: 2px;
  }
</style>
</head>
<body>

  <section class="card card--back" aria-label="Card back">
    <div class="back-mark"><span class="dot"></span><span>LEDGERWISE</span></div>
    <div class="back-url">www.ledgerwise.co</div>
  </section>

  <section class="card card--front" aria-label="Card front">
    <div class="person">
      <div class="person-name">JORDAN REYES</div>
      <div class="person-title">CEO/FOUNDER</div>
      <ul class="contact-list">
        <li><svg viewBox="0 0 16 16" aria-hidden="true"><path d="M3.5 1.5l2.5 0 1.2 3.2-1.6 1.2a8 8 0 0 0 4.5 4.5l1.2-1.6 3.2 1.2v2.5a1.5 1.5 0 0 1-1.6 1.5C6.8 13.6 2.4 9.2 2 3.1A1.5 1.5 0 0 1 3.5 1.5z"/></svg>555 214 7730</li>
        <li><svg viewBox="0 0 16 16" aria-hidden="true"><path d="M4 1h7l2 2v3H4zM2 7h12a1 1 0 0 1 1 1v5H1V8a1 1 0 0 1 1-1zm2 3v4h8v-4z"/></svg>555 318 6402</li>
        <li><svg viewBox="0 0 16 16" aria-hidden="true"><path d="M1 3h14v10H1zm1.5 1.2V5l5.5 4 5.5-4v-.8z"/></svg>hello@ledgerwise.co</li>
      </ul>
    </div>

    <div class="logo"><span class="logo-name">LEDGERWISE</span><span class="dot"></span></div>

    <div class="divider"></div>

    <div class="address">
      1420 Larkspur Court<br>
      Fairbanks, Alaska 99701
    </div>

    <svg class="bands" viewBox="0 0 640 44" aria-hidden="true">
      <polygon points="0,30 330,30 330,44 0,44" fill="var(--brand-blue)"/>
      <polygon points="318,0 640,0 640,44 296,44" fill="var(--brand-orange)"/>
    </svg>
    <div class="band-url">www.ledgerwise.co</div>
  </section>

</body>
</html>
```